Lanternway Journeys Business Card Design for Home Based Travel Agency

We already have a logo and I would like to see about getting a Business Card Design. The font on the logo can be changed. We are a home based travel agency and sell cruises and tour packages, etc. I would like the following information put into the design Name of Company and Tag Line from the logo. I would also like the email info@lanternwayjourneys.example Phone 360-728-3415. Website www.lanternwayjourneys.example. My name Neil Harper Travel Consultant and my wife's Name Marcy Harper. I would like you to use your imagination as nothing is off limites. Impress Me!

Target Market(s)

Baby Boomers

Industry/Entity Type

Travel Agent

Contact Information for Business Card

See above

Font styles to use
Serif
Sans Serif

Colors

Designer to choose colors to be used in the design.

Requirements
Must have
• Play with different fonts and needs to be easily readable, i.e. not too small of print.
Nice to have
• Use your imagination

```html
<!DOCTYPE html>
<html lang="en">
<head>
<meta charset="utf-8">
<title>Lanternway Journeys – Business Card</title>
<link rel="stylesheet" href="https://fonts.googleapis.com/css2?family=Open+Sans:wght@400;600&family=Playfair+Display:ital,wght@1,700&display=swap">
<style>
  :root {
    --backdrop: #2f2824;
    --card-front: #f7f7f5;
    --card-back: #3c3f3e;
    --ink: #1c1c1c;
    --ink-soft: #3a3a3a;
    --paper-white: #ffffff;
    --accent-orange: #f28c28;
  }
  * { margin: 0; padding: 0; box-sizing: border-box; }
  html, body { width: 1200px; height: 844px; overflow: hidden; }
  body {
    background: var(--backdrop);
    font-family: "Open Sans", Arial, sans-serif;
    position: relative;
  }
  .card {
    position: absolute;
    width: 525px;
    height: 300px;
    box-shadow: 0 12px 30px rgba(0,0,0,.45);
  }
  .card--front { left: 60px; top: 400px; background: var(--card-front); color: var(--ink); }
  .card--back  { left: 615px; top: 130px; background: var(--card-back); color: var(--paper-white); }

  .brand {
    position: absolute;
    display: flex;
    flex-direction: column;
    align-items: center;
    text-align: center;
    white-space: nowrap;
  }
  .brand__mark {
    width: 30px; height: 30px;
    background: var(--accent-orange);
    margin-bottom: 10px;
  }
  .brand__name {
    font-weight: 600;
    font-size: 26px;
    letter-spacing: .3px;
    line-height: 1.15;
  }
  .brand__tagline {
    font-size: 12px;
    margin-top: 4px;
    letter-spacing: .2px;
  }
  .card--front .brand { right: 34px; top: 28px; width: 290px; }
  .card--back .brand { left: 0; right: 0; top: 78px; }
  .card--back .brand__mark { width: 34px; height: 34px; }
  .card--back .brand__name { font-size: 34px; }
  .card--back .brand__tagline { font-size: 13px; }

  .people {
    position: absolute;
    left: 34px;
    top: 128px;
  }
  .people__name {
    font-family: "Playfair Display", Georgia, serif;
    font-style: italic;
    font-weight: 700;
    font-size: 20px;
    line-height: 1.2;
  }
  .people__name--second { padding-left: 16px; }
  .people__role { font-size: 12.5px; margin-top: 8px; color: var(--ink-soft); }

  .contact {
    position: absolute;
    left: 34px;
    bottom: 22px;
    list-style: none;
    font-size: 13px;
    color: var(--ink);
  }
  .contact__item { display: flex; align-items: center; gap: 8px; line-height: 21px; }
  .contact__icon { width: 12px; height: 12px; fill: var(--ink); flex: none; }
</style>
</head>
<body>
  <section class="card card--front" aria-label="Business card front">
    <div class="brand">
      <span class="brand__mark"></span>
      <span class="brand__name">Lanternway Journeys</span>
      <span class="brand__tagline">Every Road Leads to a Tale to Tell</span>
    </div>

    <div class="people">
      <p class="people__name">Neil Harper</p>
      <p class="people__name people__name--second">Marcy Harper</p>
      <p class="people__role">Travel Consultant</p>
    </div>

    <ul class="contact">
      <li class="contact__item">
        <svg class="contact__icon" viewBox="0 0 24 24" aria-hidden="true"><path d="M6.6 10.8a15.1 15.1 0 0 0 6.6 6.6l2.2-2.2a1 1 0 0 1 1-.25 11.4 11.4 0 0 0 3.6.57 1 1 0 0 1 1 1V20a1 1 0 0 1-1 1A17 17 0 0 1 3 4a1 1 0 0 1 1-1h3.5a1 1 0 0 1 1 1c0 1.25.2 2.45.57 3.57a1 1 0 0 1-.25 1z"/></svg>
        360-728-3415
      </li>
      <li class="contact__item">
        <svg class="contact__icon" viewBox="0 0 24 24" aria-hidden="true"><path d="M2 5h20v14H2V5zm2 2v.3l8 5.6 8-5.6V7H4z"/></svg>
        info@lanternwayjourneys.example
      </li>
      <li class="contact__item">
        <svg class="contact__icon" viewBox="0 0 24 24" aria-hidden="true"><circle cx="12" cy="12" r="10"/><path d="M2 12h20M12 2c3 3.5 3 16.5 0 20M12 2c-3 3.5-3 16.5 0 20" stroke="#f7f7f5" stroke-width="1.6" fill="none"/></svg>
        www.lanternwayjourneys.example
      </li>
    </ul>
  </section>

  <section class="card card--back" aria-label="Business card back">
    <div class="brand">
      <span class="brand__mark"></span>
      <span class="brand__name">Lanternway Journeys</span>
      <span class="brand__tagline">Every Road Leads to a Tale to Tell</span>
    </div>
  </section>
</body>
</html>
```